Compass & Canvas needs new business card design

I need a new business card design. I'm looking for out-of-the-box design which represents the freedom of being a location independent entrepreneur.
I offer coaching, retreats and trips.
I would like to see designs with and without the photo.
Colors I use are black (#000000), green (#25A796) and brown (#D7C38C)
Website compassandcanvas.net

Target Market(s)

location independent entrepreneurs, digital nomads, people looking to swap the 9 to 5 for a lifestyle business

Industry/Entity Type

Business

Contact Information for Business Card

Daria Tolsen
Your Lifestyle Business Coach, Retreat & Trip Leader
http://compassandcanvas.net
hello@compassandcanvas.net
Live a life you don't need a holiday from

Font styles to use
Serif
Sans Serif

Requirements
Must have
• One side should contain only the logo. I would also consider having the "Live a life you don't need a holiday from" on that side too (depending on how it looks)
• Please show both sides on the designs.

```html
<!DOCTYPE html>
<html lang="en">
<head>
<meta charset="utf-8">
<title>Compass &amp; Canvas – Business Card</title>
<link href="https://fonts.googleapis.com/css2?family=Libre+Baskerville&family=Montserrat:wght@400;500;700&display=swap" rel="stylesheet">
<style>
  :root {
    --ink: #000000;
    --green: #25A796;
    --sand: #D7C38C;
    --paper: #ffffff;
    --stage: #2b2b2d;
    --text: #222222;
    --rule: #9a9a9a;
  }
  * { box-sizing: border-box; margin: 0; padding: 0; }
  html, body { width: 1200px; height: 900px; overflow: hidden; }
  body {
    background: var(--stage);
    font-family: "Montserrat", Arial, sans-serif;
    color: var(--text);
    position: relative;
  }
  .card {
    position: absolute;
    width: 620px;
    height: 354px;
    background: var(--paper);
    border-radius: 26px;
    overflow: hidden;
    box-shadow: 0 14px 30px rgba(0,0,0,.45);
  }
  .card--front { left: 110px; top: 70px; }
  .card--back  { left: 470px; top: 470px; }

  /* front */
  .portrait {
    position: absolute; left: 0; top: 0; bottom: 0; width: 262px;
    background: linear-gradient(160deg, #5f8a4a 0%, #8fae6c 35%, #c9c6a4 55%, #6e8b56 75%, #4b6a3a 100%);
    border-right: 4px solid #1d1d1d;
  }
  .front-brand {
    position: absolute; left: 262px; right: 0; top: 0; bottom: 0;
  }
  .logo-name {
    font-family: "Montserrat", Arial, sans-serif;
    font-weight: 700;
    color: var(--ink);
    text-transform: uppercase;
    letter-spacing: 1px;
    line-height: 1.05;
  }
  .front-brand .logo-name {
    position: absolute; left: 48px; top: 110px; font-size: 34px;
  }
  .web {
    font-size: 15px; font-weight: 500; color: var(--text); white-space: nowrap;
  }
  .web b { color: var(--green); font-weight: 500; }
  .front-brand .web { position: absolute; right: 34px; bottom: 34px; }

  /* back */
  .back-logo {
    position: absolute; left: 40px; top: 112px; font-size: 30px;
  }
  .divider {
    position: absolute; left: 330px; top: 60px; height: 160px; width: 1px; background: var(--rule);
  }
  .contact {
    position: absolute; left: 352px; top: 58px; right: 16px;
  }
  .contact__name {
    font-family: "Libre Baskerville", Georgia, serif;
    font-weight: 400;
    color: var(--green); font-size: 24px; line-height: 1.1;
  }
  .contact__role { font-size: 14px; line-height: 1.3; margin-top: 4px; color: var(--text); }
  .contact__list { list-style: none; margin-top: 14px; font-size: 13.5px; }
  .contact__list li { display: flex; align-items: center; gap: 10px; line-height: 1.6; white-space: nowrap; }
  .contact__list svg { width: 11px; height: 11px; flex: none; }
  .contact__list b { color: var(--green); font-weight: 400; }

  .band {
    position: absolute; left: 0; right: 0; bottom: 36px; height: 18px; background: var(--green);
  }
  .motto {
    position: absolute; left: 222px; right: 36px; bottom: 30px; height: 30px;
    background: var(--ink); color: var(--paper);
    font-size: 12.5px; letter-spacing: .3px; text-transform: uppercase;
    white-space: nowrap;
    display: flex; align-items: center; justify-content: center;
  }
</style>
</head>
<body>

  <section class="card card--front" aria-label="Card front">
    <div class="portrait" role="img" aria-label="Photo of the coach sitting on a wooden fence among leafy trees, holding a small sign"></div>
    <div class="front-brand">
      <div class="logo-name">Compass<br>&amp; Canvas</div>
      <p class="web">www.<b>compassandcanvas</b>.net</p>
    </div>
  </section>

  <section class="card card--back" aria-label="Card back">
    <div class="logo-name back-logo">Compass<br>&amp; Canvas</div>
    <div class="divider"></div>
    <div class="contact">
      <h1 class="contact__name">Daria Tolsen</h1>
      <p class="contact__role">Your Lifestyle Business Coach<br>Retreat &amp; Trip Leader</p>
      <ul class="contact__list">
        <li>
          <svg viewBox="0 0 12 12"><path d="M2.5 1 L4.5 1 L5.2 3.4 L4 4.4 Q5 6.8 7.6 8 L8.6 6.8 L11 7.5 L11 9.5 Q10.5 11 9 11 Q1 10 1 2.8 Q1 1.3 2.5 1 Z" fill="var(--green)"/></svg>
          <span>+330 5510-2394</span>
        </li>
        <li>
          <svg viewBox="0 0 12 12"><rect x="1" y="2.5" width="10" height="7" fill="none" stroke="var(--green)" stroke-width="1.3"/><path d="M1 2.5 L6 6.5 L11 2.5" fill="none" stroke="var(--green)" stroke-width="1.3"/></svg>
          <span>hello@compassandcanvas.net</span>
        </li>
        <li>
          <svg viewBox="0 0 12 12"><circle cx="6" cy="6" r="5" fill="none" stroke="var(--green)" stroke-width="1.2"/><ellipse cx="6" cy="6" rx="2.2" ry="5" fill="none" stroke="var(--green)" stroke-width="1"/><path d="M1 6 H11" stroke="var(--green)" stroke-width="1"/></svg>
          <span>www.<b>compassandcanvas</b>.net</span>
        </li>
      </ul>
    </div>
    <div class="band"></div>
    <p class="motto">Live a life you don't need a holiday from</p>
  </section>

</body>
</html>
```